Accounting Firm

We are a two partner accounting firm. our business name is VELLOR & BRISKETT. We are accountants and business consultants.

We need a stationery design for our letterhead, with compliments slip, business card and envelope.

We'd like clean, professional look. I'm 39 years old and my partner is 60+, so we'd like modern yet elegant design. Dark Navy Blue as a primary colour is preferred.

Thank you.

Hi Guys

No logo.

Thanks

Accounting

• Firm name :VELLOR & BRISKETT
Business Consultants & Accountants
Address: Level 1 Units 5 & 6, 27 Marrow Crescent NORWOOD SA 5067
Box address: PO Box 318 KENT TOWN SA 5071
telp: +61 8 8194 6027
fax: +61 8 8456 2719

Dominic Vellor, CA
Lucas Briskett, CPA

dominic.vellor@vellorbriskett.example.au
lucas.briskett@vellorbriskett.example.au

Dark Navy Blue as primary colour

```html
<!DOCTYPE html>
<html lang="en">
<head>
<meta charset="utf-8">
<title>Vellor &amp; Briskett — Business Card</title>
<link rel="stylesheet" href="https://fonts.googleapis.com/css2?family=Source+Sans+3:wght@400;600&display=swap">
<style>
  :root {
    --page-bg: #2a2a2c;
    --card-white: #f4f4f4;
    --card-white-edge: #e2e2e2;
    --ink-grey: #6a6a6a;
    --ink-name: #5b6470;
    --brand-blue: #1f6fc4;
    --band-light: #1c8fdc;
    --band-dark: #0b4aa0;
    --back-light: #1a9be0;
    --back-dark: #0a4c9e;
    --white: #ffffff;
  }
  * { box-sizing: border-box; margin: 0; padding: 0; }
  html, body {
    width: 900px; height: 1200px; overflow: hidden;
    background: var(--page-bg);
    font-family: "Source Sans 3", "Myriad Pro", Arial, sans-serif;
  }
  .canvas { position: relative; width: 900px; height: 1200px; }

  .card {
    position: absolute; left: 100px; width: 706px; height: 406px;
    box-shadow: 0 8px 24px rgba(0,0,0,0.45);
    overflow: hidden;
  }

  /* Front */
  .card--front {
    top: 92px;
    background: radial-gradient(ellipse at 45% 30%, var(--white) 0%, var(--card-white) 45%, var(--card-white-edge) 100%);
  }
  .brand { position: absolute; left: 12px; top: 12px; }
  .brand__square {
    position: absolute; left: 0; top: 0; width: 40px; height: 40px;
    background: var(--brand-blue);
  }
  .brand__name {
    position: absolute; left: 88px; top: 78px; white-space: nowrap;
    font-size: 21px; font-weight: 400; color: var(--ink-name); letter-spacing: 0.2px;
  }
  .brand__tagline {
    position: absolute; left: 88px; top: 106px; white-space: nowrap;
    font-size: 13.5px; color: var(--ink-grey);
  }
  .address {
    position: absolute; left: 410px; top: 20px;
    font-size: 15px; line-height: 26.5px; color: var(--ink-grey);
    list-style: none;
  }
  .person { position: absolute; left: 100px; top: 235px; }
  .person__name { font-size: 23px; font-weight: 600; color: var(--ink-grey); line-height: 1.1; }
  .person__role { font-size: 14.5px; color: var(--ink-grey); margin-top: 2px; }
  .contact {
    position: absolute; left: 410px; top: 237px;
    font-size: 15px; line-height: 28.5px; color: var(--ink-grey);
    list-style: none;
  }
  .contact__label { display: inline-block; width: 23px; }
  .band {
    position: absolute; left: 0; right: 0; bottom: 0; height: 59px;
    background: linear-gradient(90deg, var(--band-light), var(--band-dark));
    display: flex; align-items: center; justify-content: center;
    color: var(--white); font-size: 15px; letter-spacing: 0.2px;
  }

  /* Back */
  .card--back { top: 702px; width: 710px; height: 408px; }
  .back__field {
    position: absolute; inset: 0;
    background: radial-gradient(ellipse at 15% 5%, var(--back-light) 0%, #157fce 40%, var(--back-dark) 100%);
  }
  .back__mark {
    position: absolute; left: 0; right: 0; top: 180px;
    display: flex; align-items: center; justify-content: center; gap: 14px;
  }
  .back__square { width: 34px; height: 34px; background: var(--white); }
  .back__name { font-size: 30px; font-weight: 400; color: var(--white); letter-spacing: 0.5px; }
</style>
</head>
<body>
<main class="canvas">

  <section class="card card--front" aria-label="Business card front">
    <div class="brand">
      <span class="brand__square"></span>
      <span class="brand__name">VELLOR &amp; BRISKETT</span>
      <span class="brand__tagline">Business Consultants &amp; Accountants</span>
    </div>

    <ul class="address">
      <li>PO Box 318 KENT TOWN SA 5071</li>
      <li>Level 1 Units 5 &amp; 6, 27 Marrow Crescent</li>
      <li>NORWOOD SA 5067</li>
    </ul>

    <div class="person">
      <p class="person__name">Dominic Vellor</p>
      <p class="person__role">Business consultants</p>
    </div>

    <ul class="contact">
      <li><span class="contact__label">P:</span>+61 8 8194 6027</li>
      <li><span class="contact__label">F:</span>+61 8 8456 2719</li>
      <li><span class="contact__label">E:</span>dominic@vellorbriskett.example.au</li>
    </ul>

    <div class="band">www.vellorbriskett.example.au</div>
  </section>

  <section class="card card--back" aria-label="Business card back">
    <div class="back__field" role="img" aria-label="Blue tiled brand pattern background"></div>
    <div class="back__mark">
      <span class="back__square"></span>
      <span class="back__name">VELLOR &amp; BRISKETT</span>
    </div>
  </section>

</main>
</body>
</html>
```